Web Page for The Marlow Law Firm

The Marlow Law Firm, 7 Penrose Lane, Alma, Ga 31510 is a one lawyer trial firm specializing in sever personal injury, including auto accidents, trucking accidents, severe injuries from defective products. Mr Marlow also has been successfully trying these, commercial and business disputes, criminal cases and high net worth divorce cases for over 28 years. He has tried over 100 cases to a jury verdict.

Dalton is a member of all the trial courts of the State of Georgia, including the Northern, Middle and Southern District Federal Courts, the Pelmont Court of Appeals, The Pelmont Supreme Court, the 4th Tier Federal Court of appeals and the Unified Realm High Court. Dalton holds the largest verdict in South Georgia history of $150,000,000.00. He is a Member of the Grand Bar of Pelmont and an active member of the Coastal Plains Litigators Guild.

Dalton R. Marlow graduated from Wexley Ridge High School in Alma, Georgia in 1978. He received his BBA in Accounting in 1982 and graduated cum laude from the Halvern Plains School of Law in 1986 with a J.D.

Industry/Entity Type

Lawyer

Number of Pages Required

4 page

Requirements
Must have
• Introduction to firm; separate biography of principal; representative cases; testemonials; blog; method of contact

```html
<!DOCTYPE html>
<html lang="en">
<head>
<meta charset="utf-8">
<title>The Marlow Law Firm</title>
<link href="https://fonts.googleapis.com/css2?family=Raleway:wght@300;400;500;600;700&family=Open+Sans:wght@400;600;700&display=swap" rel="stylesheet">
<style>
:root{
  --cream:#f5ecd7;
  --cream-light:#fdf6e6;
  --field:#f3e8cf;
  --dark:#3a302a;
  --ink:#2f2925;
  --muted:#8a8178;
  --line:#e6dbc2;
  --white:#fffaf0;
}
*{margin:0;padding:0;box-sizing:border-box}
html,body{width:972px;height:1200px;overflow:hidden;background:var(--cream)}
body{font-family:"Open Sans",sans-serif;color:var(--ink);position:relative}

/* header */
.site-header{position:absolute;left:0;top:0;width:972px;height:70px;background:var(--cream)}
.brand{position:absolute;left:160px;top:16px;display:flex;align-items:center;gap:9px}
.brand-mark{width:28px;height:28px;border-radius:50%;background:var(--dark)}
.brand-name{font-family:"Raleway",sans-serif;font-weight:600;font-size:19px;line-height:20px;color:var(--dark)}
.call{position:absolute;right:160px;top:20px;display:flex;gap:6px;align-items:flex-start}
.call-text{text-align:right;font-family:"Raleway",sans-serif;color:var(--dark)}
.call-text .lead{font-size:12.5px;line-height:14px}
.call-text .number{font-family:"Open Sans",sans-serif;font-weight:700;font-size:17px;line-height:18px}

/* nav */
.main-nav{position:absolute;left:0;top:70px;width:972px;height:34px;background:var(--cream-light)}
.nav-item{position:absolute;top:0;height:34px;line-height:34px;font-size:10.5px;color:var(--ink);transform:translateX(-50%)}
.nav-item.active{transform:none;left:160px;width:69px;text-align:center;background:var(--dark);color:#fff}
.search{position:absolute;left:674px;top:6px;width:138px;height:21px;border:1px solid var(--line);background:#fffbf2;font-size:8.5px;color:var(--muted);line-height:19px;padding-left:6px}
.search svg{position:absolute;right:5px;top:4px}

/* hero */
.hero{position:absolute;left:0;top:104px;width:972px;height:346px;
  background:
   radial-gradient(ellipse 170px 150px at 520px 210px,#2a1a12 0%,rgba(60,30,20,.8) 55%,rgba(0,0,0,0) 100%),
   radial-gradient(ellipse 200px 180px at 830px 240px,rgba(60,45,35,.8),rgba(0,0,0,0) 100%),
   radial-gradient(ellipse 140px 220px at 40px 260px,#9a6a22,rgba(0,0,0,0) 100%),
   linear-gradient(90deg,#b07a2c 0%,#d9a650 30%,#e9c27a 55%,#d7a557 75%,#c99548 100%)}
.hero-caption{position:absolute;left:160px;top:122px;width:208px;height:104px;background:rgba(62,56,52,.8);color:#fff;font-family:"Raleway",sans-serif;padding:22px 0 0 45px}
.hero-caption .a{font-weight:300;font-size:20px;line-height:20px}
.hero-caption .b{font-weight:700;font-size:20px;line-height:20px}
.hero-caption .c{font-weight:400;font-size:15.5px;line-height:22px;padding-left:4px}
.hero-dots{position:absolute;left:160px;top:326px;display:flex;gap:8px}
.hero-dots span{width:13px;height:13px;background:#f3e7cb}
.hero-dots span.on{background:var(--dark)}

/* intro */
.intro{position:absolute;left:0;top:450px;width:972px;height:140px;background:var(--cream);text-align:center}
.intro h1{font-family:"Raleway",sans-serif;font-weight:400;font-size:20px;margin-top:38px;color:var(--ink)}
.intro h1 b{font-weight:700}
.intro p{font-size:10px;line-height:17px;margin-top:5px;color:var(--ink)}

/* services */
.services{position:absolute;left:0;top:590px;width:972px;height:138px;background:var(--cream-light)}
.service{position:absolute;top:48px;width:210px}
.service .icon{position:absolute;left:0;top:0;width:42px;height:42px;border-radius:50%;background:var(--dark);display:flex;align-items:center;justify-content:center}
.service h3{position:absolute;left:47px;top:0;font-family:"Raleway",sans-serif;font-weight:600;font-size:12.5px;color:var(--ink);white-space:nowrap}
.service p{position:absolute;left:48px;top:18px;width:160px;font-size:8.5px;line-height:12.5px;color:var(--muted)}
.read-more{font-size:8.5px;color:var(--ink);display:flex;align-items:center;gap:5px}
.service .read-more{position:absolute;left:48px;top:45px}

/* biography */
.biography{position:absolute;left:0;top:728px;width:972px;height:208px;background:var(--cream)}
.portrait{position:absolute;left:159px;top:34px;width:139px;height:139px;background:linear-gradient(135deg,#5a3a24 0%,#7b5634 40%,#d9d2c4 75%,#f2ece0 100%)}
.bio-body{position:absolute;left:312px;top:36px;width:270px}
.bio-body h2{font-family:"Raleway",sans-serif;font-weight:500;font-size:16px;color:var(--ink)}
.bio-body p{font-size:8.5px;line-height:12.5px;color:var(--muted);margin-top:6px}
.bio-body p+p{margin-top:1px}
.bio-body .read-more{margin-top:11px}
.cases{position:absolute;left:659px;top:29px;width:153px}
.cases h3{background:var(--white);height:36px;line-height:36px;padding-left:7px;font-family:"Raleway",sans-serif;font-weight:500;font-size:11.5px;color:var(--ink)}
.cases li{list-style:none;background:var(--white);height:21px;margin-top:2px;display:flex;align-items:center;gap:6px;padding-left:7px;font-size:8.5px;color:var(--ink)}

/* lower band */
.lower{position:absolute;left:0;top:936px;width:972px;height:228px;background:var(--cream-light)}
.section-title{position:absolute;font-family:"Raleway",sans-serif;font-weight:400;font-size:14px;color:var(--ink)}
.news-item{position:absolute;left:160px;width:220px;height:42px}
.date{position:absolute;left:0;top:0;width:41px;height:42px;background:var(--dark);color:#fff;text-align:center;font-family:"Raleway",sans-serif}
.date::after{content:"";position:absolute;right:-6px;top:15px;border-left:6px solid var(--dark);border-top:6px solid transparent;border-bottom:6px solid transparent}
.date .d{font-weight:700;font-size:15px;line-height:17px;padding-top:5px}
.date .m{font-size:11px;line-height:13px}
.news-item h4{position:absolute;left:55px;top:0;font-family:"Raleway",sans-serif;font-weight:500;font-size:10px;white-space:nowrap}
.news-item p{position:absolute;left:55px;top:14px;font-size:8.5px;line-height:12.5px;width:130px}
.quote{position:absolute;left:382px;top:54px;width:208px;height:82px;background:var(--field);padding:12px 10px 0 22px;font-size:8.5px;line-height:12.5px;color:var(--muted)}
.quote::after{content:"";position:absolute;left:26px;bottom:-10px;border-top:10px solid var(--field);border-right:14px solid transparent}
.quote svg{position:absolute;left:8px;top:11px}
.quote-name{position:absolute;left:385px;top:159px;font-size:8.5px}
.quote-dots{position:absolute;left:563px;top:185px;display:flex;gap:4px}
.quote-dots span{width:6px;height:6px;border-radius:50%;background:#eadfc6}
.quote-dots span.on{background:var(--dark)}
.field{position:absolute;left:626px;width:186px;background:var(--field);font-size:8.5px;color:var(--ink);padding:6px 9px}
.submit{position:absolute;left:742px;top:188px;width:68px;height:20px;background:var(--dark);color:#fff;font-size:9px;line-height:20px;text-align:center}

/* footer */
.site-footer{position:absolute;left:0;top:1164px;width:972px;height:36px;background:var(--cream)}
.site-footer .copy{position:absolute;left:160px;top:12px;font-size:8.5px}
.social{position:absolute;right:159px;top:10px;display:flex;gap:6px}
.social span{width:16px;height:16px;border-radius:3px;background:var(--dark)}
</style>
</head>
<body>

<header class="site-header">
  <div class="brand">
    <span class="brand-mark"></span>
    <div class="brand-name">The Marlow<br>Law Firm</div>
  </div>
  <div class="call">
    <svg width="24" height="24" viewBox="0 0 24 24" aria-hidden="true">
      <rect width="24" height="24" rx="4" fill="#3a302a"/>
      <path d="M8 5c1 0 2 2.5 2 3.3 0 .8-1.3 1.2-1.1 2 .4 1.6 2.3 3.5 3.8 3.9.8.2 1.2-1.1 2-1.1.8 0 3.3 1 3.3 2 0 1.3-1.4 3-3 3C10 18 6 14 6 9c0-1.6 1-4 2-4z" fill="#f5ecd7"/>
    </svg>
    <div class="call-text">
      <div class="lead">Call now to find out how:</div>
      <div class="number">+ 555 010 482 19</div>
    </div>
  </div>
</header>

<nav class="main-nav">
  <div class="nav-item active">Home</div>
  <div class="nav-item" style="left:266px">About Us</div>
  <div class="nav-item" style="left:346px">Paratcie</div>
  <div class="nav-item" style="left:418px">Service</div>
  <div class="nav-item" style="left:485px">Blog</div>
  <div class="nav-item" style="left:560px">Contact Us</div>
  <div class="search">Search Here...
    <svg width="11" height="11" viewBox="0 0 11 11" aria-hidden="true"><circle cx="4.5" cy="4.5" r="3.3" fill="none" stroke="#5a4f46" stroke-width="1.4"/><path d="M7 7l3 3" stroke="#5a4f46" stroke-width="1.6"/></svg>
  </div>
</nav>

<section class="hero" role="img" aria-label="Photo of a stack of law books in a warm, gilded hall with people in the background">
  <div class="hero-caption">
    <div class="a">Welcome to</div>
    <div class="b">The Marlow</div>
    <div class="c">Law Firm</div>
  </div>
  <div class="hero-dots"><span></span><span></span><span></span><span class="on"></span></div>
</section>

<section class="intro">
  <h1>Welcome to <b>The Marlow</b> Law Firm</h1>
  <p>Lorem Ipsum is simply dummy text of the printing and typesetting industry. Lorem Ipsum has been<br>the industry's&nbsp; dummy text ever since the 1500s, when an unknown printer took a galley.</p>
</section>

<section class="services">
  <div class="service" style="left:160px">
    <div class="icon"><svg width="16" height="16" viewBox="0 0 16 16" aria-hidden="true"><rect x="5" y="1" width="7" height="5" transform="rotate(45 8.5 3.5)" fill="#fff"/><path d="M6 8l-4 5" stroke="#fff" stroke-width="2.4" stroke-linecap="round"/></svg></div>
    <h3>CRIMINAL DEFENCE</h3>
    <p>Lorem Ipsum is simply dummy text of the printing and typesetting industry</p>
    <div class="read-more">Read More <svg width="10" height="6" viewBox="0 0 10 6"><path d="M0 3h8M6 .5L9 3 6 5.5" stroke="#2f2925" stroke-width="1.2" fill="none"/></svg></div>
  </div>
  <div class="service" style="left:382px">
    <div class="icon"><svg width="16" height="14" viewBox="0 0 16 14" aria-hidden="true"><rect x="1" y="3" width="14" height="10" rx="1.5" fill="#fff"/><rect x="5.5" y="0.8" width="5" height="3" rx="1" fill="none" stroke="#fff" stroke-width="1.3"/></svg></div>
    <h3>BUSINESS LAW</h3>
    <p>Lorem Ipsum is simply dummy text of the printing and typesetting industry</p>
    <div class="read-more">Read More <svg width="10" height="6" viewBox="0 0 10 6"><path d="M0 3h8M6 .5L9 3 6 5.5" stroke="#2f2925" stroke-width="1.2" fill="none"/></svg></div>
  </div>
  <div class="service" style="left:604px">
    <div class="icon"><svg width="18" height="16" viewBox="0 0 18 16" aria-hidden="true"><path d="M9 0L1 4h16z" fill="#fff"/><rect x="1" y="4.5" width="16" height="1.5" fill="#fff"/><rect x="3" y="7" width="2" height="6" fill="#fff"/><rect x="8" y="7" width="2" height="6" fill="#fff"/><rect x="13" y="7" width="2" height="6" fill="#fff"/><rect x="1" y="13.5" width="16" height="2" fill="#fff"/></svg></div>
    <h3>CRIMINAL DEFENCE</h3>
    <p>Lorem Ipsum is simply dummy text of the printing and typesetting industry</p>
    <div class="read-more">Read More <svg width="10" height="6" viewBox="0 0 10 6"><path d="M0 3h8M6 .5L9 3 6 5.5" stroke="#2f2925" stroke-width="1.2" fill="none"/></svg></div>
  </div>
</section>

<section class="biography">
  <div class="portrait" role="img" aria-label="Portrait of the principal lawyer reading at a desk in front of law book shelves"></div>
  <div class="bio-body">
    <h2>Separate Biography of Principal</h2>
    <p>Lorem Ipsum is simply dummy text of the printing and typesetting industry. Lorem Ipsum has been the industry's standard dummy text ever since the 1500s, when an unknown printer took a galley of type and scrambled it</p>
    <p>Lorem Ipsum is simply dummy text of the printing and typesetting industry. Lorem Ipsum has been the industry's standard dummy text ever since the 1500s.</p>
    <div class="read-more">Read More <svg width="10" height="6" viewBox="0 0 10 6"><path d="M0 3h8M6 .5L9 3 6 5.5" stroke="#2f2925" stroke-width="1.2" fill="none"/></svg></div>
  </div>
  <div class="cases">
    <h3>REPRESENTATIVE CASES</h3>
    <ul>
      <li><svg width="10" height="6" viewBox="0 0 10 6"><path d="M0 3h8M6 .5L9 3 6 5.5" stroke="#2f2925" stroke-width="1.2" fill="none"/></svg>FAMILY LAW</li>
      <li><svg width="10" height="6" viewBox="0 0 10 6"><path d="M0 3h8M6 .5L9 3 6 5.5" stroke="#2f2925" stroke-width="1.2" fill="none"/></svg>EMPLOYMENT LAW</li>
      <li><svg width="10" height="6" viewBox="0 0 10 6"><path d="M0 3h8M6 .5L9 3 6 5.5" stroke="#2f2925" stroke-width="1.2" fill="none"/></svg>IMMIGRATION LAW</li>
      <li><svg width="10" height="6" viewBox="0 0 10 6"><path d="M0 3h8M6 .5L9 3 6 5.5" stroke="#2f2925" stroke-width="1.2" fill="none"/></svg>BUSINESS LAW</li>
      <li><svg width="10" height="6" viewBox="0 0 10 6"><path d="M0 3h8M6 .5L9 3 6 5.5" stroke="#2f2925" stroke-width="1.2" fill="none"/></svg>INSURENCE LAW</li>
    </ul>
  </div>
</section>

<section class="lower">
  <h2 class="section-title" style="left:159px;top:31px">LATEST NEWS</h2>
  <div class="news-item" style="top:59px">
    <div class="date"><div class="d">02</div><div class="m">DEC</div></div>
    <h4>LOREM IPSUM IS SIMPLY DUMMY</h4>
    <p>Lorem Ipsum is simply dummy and typesetting try.</p>
  </div>
  <div class="news-item" style="top:108px">
    <div class="date"><div class="d">02</div><div class="m">DEC</div></div>
    <h4>LOREM IPSUM IS SIMPLY DUMMY</h4>
    <p>Lorem Ipsum is simply dummy and typesetting try.</p>
  </div>
  <div class="news-item" style="top:157px">
    <div class="date"><div class="d">02</div><div class="m">DEC</div></div>
    <h4>LOREM IPSUM IS SIMPLY DUMMY</h4>
    <p>Lorem Ipsum is simply dummy and typesetting try.</p>
  </div>

  <h2 class="section-title" style="left:381px;top:30px">TESTIMONIALS</h2>
  <div class="quote">
    <svg width="8" height="7" viewBox="0 0 8 7" aria-hidden="true"><path d="M0 7V4C0 1.5 1 .5 3 0v1.3C2 1.7 1.7 2.4 1.7 3.3H3.4V7zM4.6 7V4C4.6 1.5 5.6.5 7.6 0v1.3C6.6 1.7 6.3 2.4 6.3 3.3H8V7z" fill="#3a302a"/></svg>
    Lorem Ipsum is simply dummy text of the printing and typesetting industry. Lorem Ipsum has been the ndustry's standard dummy text ever since the 1500s,
  </div>
  <div class="quote-name">Jhon Tarrow (New York)</div>
  <div class="quote-dots"><span></span><span class="on"></span><span></span></div>

  <h2 class="section-title" style="left:626px;top:30px;font-size:17px;font-weight:500">Contact From</h2>
  <div class="field" style="top:54px;height:21px">Enter Your Name:</div>
  <div class="field" style="top:82px;height:21px">Enter Your Email:</div>
  <div class="field" style="top:110px;height:68px">Enter Your Comments:</div>
  <div class="submit">Submit</div>
</section>

<footer class="site-footer">
  <div class="copy">The Marlow Law Firm © 2014 | Privacy policy</div>
  <div class="social"><span></span><span></span><span></span></div>
</footer>

</body>
</html>
```